Postcard Design

Qelvaro is a medical sales and communication network between doctors and doctors, doctors and sales representatives and doctors and medical companies. Doctors offices are off limits to sales reps. Communication takes place on a closed network of computer tablets. Doctors,Companies and Sale Representatives must join the the Qelvaro network and then they begin to send short videos or messages or pdf files to those doctors in their territory. Doctors will post the Qel varo logo on their doors, restricting sales reps from waiting in offices to make cold calls. They receive permission for office visits
through the tablet based platform.

Industry/Entity Type

Communication

```html
<!DOCTYPE html>
<html lang="en">
<head>
<meta charset="UTF-8">
<title>Qelvaro – Sales Representative Restricted Office</title>
<link rel="stylesheet" href="https://fonts.googleapis.com/css2?family=Ubuntu:wght@500;700&family=Arimo:wght@400&display=swap">
<style>
  :root {
    --stage: #e8e4de;
    --navy: #0f3b57;
    --navy-deep: #0a2a40;
    --ink: #03121d;
    --sky: #8fd4f4;
    --ring: #2a8fd6;
    --ring-light: #6cc0ee;
    --white: #f2f6f9;
    --photo-light: #eef0f2;
    --photo-mid: #c9ccd0;
  }
  * { margin: 0; padding: 0; box-sizing: border-box; }
  html, body { width: 1200px; height: 873px; overflow: hidden; background: var(--stage); }
  .canvas { position: relative; width: 1200px; height: 873px; }
  .postcard {
    position: absolute; left: 301px; top: 20px;
    width: 622px; height: 866px;
    transform: scale(0.962); transform-origin: top left;
    background: radial-gradient(circle at 50% 52%, #174c6d 0%, var(--navy) 45%, var(--navy-deep) 100%);
    overflow: hidden;
  }
  .headline {
    position: absolute; top: 36px; left: 0; width: 100%;
    text-align: center; font-family: "Ubuntu", sans-serif; font-weight: 700;
    font-size: 43px; line-height: 42px; color: var(--sky); letter-spacing: 0.3px;
  }
  .divider {
    position: absolute; top: 125px; left: 55px; width: 514px;
    border-top: 2px dotted rgba(230, 240, 248, 0.75);
  }
  .instructions {
    position: absolute; top: 132px; left: 0; width: 100%;
    text-align: center; font-family: "Arimo", sans-serif; font-size: 20px;
    line-height: 26px; color: var(--white);
  }
  .emblem { position: absolute; left: 0; top: 180px; width: 622px; height: 560px; }
  .brand {
    position: absolute; top: 718px; left: 66px;
    display: flex; align-items: center; gap: 14px;
  }
  .brand-mark { width: 38px; height: 38px; border: 4px solid var(--ring-light); border-radius: 50%; }
  .brand-name {
    font-family: "Ubuntu", sans-serif; font-weight: 700; font-size: 46px;
    line-height: 48px; color: var(--sky); letter-spacing: 0.5px;
  }
  .tagline {
    position: absolute; top: 767px; left: 170px;
    font-family: "Ubuntu", sans-serif; font-weight: 700; font-size: 18px; color: var(--sky);
  }
  .web-band {
    position: absolute; top: 806px; left: 0; width: 100%; height: 32px;
    background: var(--ink); text-align: center;
    font-family: "Arimo", sans-serif; font-size: 19px; line-height: 32px;
    color: var(--white); letter-spacing: 5px;
  }
</style>
</head>
<body>
<div class="canvas">
  <section class="postcard">
    <h1 class="headline">SALES REPRESENTATIVE<br>RESTRICTIED OFFICE</h1>
    <div class="divider"></div>
    <p class="instructions">PICK UP SALE REPRESENTATIVE PACKET<br>AT FRONT DESK OR SIGN UP AT</p>

    <svg class="emblem" viewBox="0 0 622 560" aria-hidden="false">
      <defs>
        <radialGradient id="photoTone" cx="55%" cy="40%" r="65%">
          <stop offset="0%" stop-color="var(--photo-light)"/>
          <stop offset="100%" stop-color="var(--photo-mid)"/>
        </radialGradient>
      </defs>
      <circle cx="311" cy="271" r="300" fill="none" stroke="#0b2d44" stroke-width="22" opacity="0.7"/>
      <circle cx="311" cy="271" r="270" fill="var(--ink)" opacity="0.85"/>
      <circle cx="311" cy="271" r="250" fill="var(--ring)"/>
      <circle cx="311" cy="271" r="238" fill="var(--ring-light)"/>
      <circle cx="311" cy="271" r="230" fill="url(#photoTone)" role="img"
        aria-label="Photo: a doctor's hand holding up a stethoscope whose chest piece is a small clock face"/>
    </svg>

    <div class="brand">
      <span class="brand-mark"></span>
      <span class="brand-name">QELVARO</span>
    </div>
    <p class="tagline">Leaders in Healthcare Communication</p>
    <div class="web-band">www.qelvaro.com</div>
  </section>
</div>
</body>
</html>
```